Birchway Contracting website

I need a website for my construction. I want customers to see past builds and current projects Something that stands out and reflects awareness, safety, attention to details. I already have a logo designed by Studio Marrowfield
Target Market(s)
Residential and Commercial sectors
Industry/Entity Type
Construction
Logo Text
Birchway Contracting
Colors
EB3D1F
EC4F4E
F09395
F8D3D4
FCEDEE
Requirements
Must have
- My contact info
Nice to have
- Past projects

```html
<!DOCTYPE html>
<html lang="en">
<head>
<meta charset="utf-8">
<title>Birchway Contracting</title>
<link rel="stylesheet" href="https://fonts.googleapis.com/css2?family=Roboto:wght@400;500;700&display=swap">
<style>
:root{
  --red:#eb3d1f;
  --red-bright:#e8241b;
  --red-soft:#ec4f4e;
  --pink:#f09395;
  --blush:#f8d3d4;
  --mist:#fcedee;
  --ink:#111;
  --text:#444;
  --white:#fff;
  --line:#ddd;
}
*{box-sizing:border-box;margin:0;padding:0}
html,body{width:1200px;height:4747px;overflow:hidden}
body{font-family:"Roboto",Arial,sans-serif;color:var(--ink);background:var(--white);position:relative}
.section{position:relative;width:1200px;overflow:hidden}
.abs{position:absolute}
.photo{position:absolute}
.btn{position:absolute;background:var(--red-bright);color:var(--white);font-size:15px;font-weight:500;display:flex;align-items:center;justify-content:center}
.vline{position:absolute;left:116px;width:2px;background:var(--red-soft)}
.band{background:linear-gradient(180deg,#ea3a22 0%,#e5261c 55%,#d9241c 100%)}
.band-title{position:absolute;left:0;width:1200px;text-align:center;color:var(--white);font-size:37px;font-weight:700}
.section-title{position:absolute;font-size:36px;font-weight:700;text-transform:uppercase}

/* header */
.hero{height:682px}
.hero-photo{left:0;top:0;width:1200px;height:682px;background:linear-gradient(120deg,#3d3f44 0%,#6d6e70 40%,#8e8c86 60%,#4b4a47 100%)}
.topbar{position:absolute;left:0;top:0;width:1200px;height:74px;background:rgba(20,20,20,.55)}
.brand{position:absolute;left:112px;top:22px;color:var(--white);font-size:28px;font-weight:700;letter-spacing:1px;display:flex;align-items:center;gap:10px}
.brand .mark{width:18px;height:18px;background:var(--red)}
.nav{position:absolute;top:28px;left:0;display:flex;font-size:15px;font-weight:500;color:var(--white)}
.nav span{position:absolute;white-space:nowrap}
.nav .active{color:var(--red-bright)}
.hero-bar{left:112px;top:295px;width:10px;height:166px;background:var(--red-bright)}
.hero-title{left:147px;top:310px;color:var(--white);font-size:41px;font-weight:700}
.hero-text{left:148px;top:367px;width:430px;color:var(--white);font-size:16px;line-height:25px;font-weight:500}
.dots{position:absolute;display:flex;gap:10px}
.dots i{width:11px;height:11px;border-radius:50%;border:1.5px solid var(--white);display:block}
.dots i.on{background:var(--white)}

/* welcome */
.welcome{height:586px}
.welcome-title{left:121px;top:102px;font-size:34px;font-weight:700;line-height:42px}
.welcome-text{left:121px;top:200px;width:450px;font-size:13.5px;line-height:28.5px;color:var(--text)}
.welcome-photo{left:627px;top:85px;width:462px;height:414px;background:linear-gradient(160deg,#6d8fb3 0%,#a8bfd6 40%,#8a8478 75%,#5a5550 100%)}

/* services */
.services{height:535px}
.service{position:absolute;top:153px;width:234px;height:297px}
.service span{position:absolute;left:0;width:100%;text-align:center;color:var(--white);font-size:20px;font-weight:700}

/* news */
.news{height:723px}
.news-card{position:absolute;top:138px;width:467px;height:502px;border:1px solid var(--line);background:var(--white)}
.news-card .photo{left:0;top:0;width:465px;height:289px}
.news-card h3{position:absolute;left:19px;top:308px;font-size:25px;font-weight:500}
.news-card p{position:absolute;left:20px;top:350px;width:430px;font-size:13.5px;line-height:25.5px;color:var(--text)}
.news-card .btn{left:22px;top:443px;width:138px;height:40px}

/* projects */
.projects{height:687px}
.projects .sub{position:absolute;top:128px;width:1200px;text-align:center;color:var(--white);font-size:16px}
.filters{position:absolute;top:180px;left:0;width:1200px;color:var(--white);font-size:15px;font-weight:500}
.filters span{position:absolute;white-space:nowrap}
.filters .on{text-decoration:underline}
.project{position:absolute;top:232px;width:308px;height:324px}
.project span{position:absolute;left:20px;bottom:20px;color:var(--white);font-size:20px;font-weight:700}
.project-info{background:#161a22}
.project-info h4{position:absolute;left:28px;top:42px;color:var(--white);font-size:20px;font-weight:700}
.project-info p{position:absolute;left:30px;top:82px;width:250px;color:#e6e6e6;font-size:14.5px;line-height:34px}

/* team */
.team{height:590px}
.member{position:absolute;top:144px;width:234px}
.member .photo{position:relative;width:234px;height:300px}
.member h5{margin-top:12px;font-size:20px;font-weight:700}
.member .rule{width:175px;height:2px;background:var(--red-bright);margin-top:4px}
.member p{margin-top:8px;font-size:15px;color:var(--text)}

/* contact */
.contact{height:573px}
.field{position:absolute;background:var(--white);font-size:14px;color:#333;padding:0 12px;display:flex;align-items:center}
.field.area{align-items:flex-start;padding-top:18px}
.submit{position:absolute;left:503px;top:437px;width:194px;height:51px;border:2px solid var(--white);color:var(--white);font-size:14px;font-weight:700;display:flex;align-items:center;justify-content:center}

/* footer */
.footer{height:368px;background:var(--white)}
.foot-brand{left:115px;top:82px;color:var(--red-bright);font-size:32px;font-weight:700;display:flex;align-items:center;gap:10px}
.foot-brand .mark{width:18px;height:18px;background:var(--red-bright)}
.socials{position:absolute;left:139px;top:151px;display:flex;gap:12px}
.socials i{width:32px;height:32px;border-radius:50%;background:#1f3a80;display:block}
.socials i:nth-child(2){background:#c3206e}
.socials i:nth-child(3){background:#1c6fc4}
.socials i:nth-child(4){background:#2a3c8e}
.foot-col{position:absolute;top:66px}
.foot-col h6{font-size:17px;font-weight:700}
.foot-col .rule{width:40px;height:2px;background:var(--red-bright);margin:8px 0 12px}
.foot-col ul{list-style:none;font-size:14px;color:#333;line-height:27px}
.contact-row{display:flex;gap:12px;align-items:flex-start;font-size:14px;color:#333;line-height:22px;margin-bottom:22px}
.contact-row svg{flex:none}
.foot-rule{position:absolute;left:112px;top:311px;width:976px;height:1px;background:var(--line)}
.copy{position:absolute;left:0;top:334px;width:1200px;text-align:center;font-size:14px;color:#333}
</style>
</head>
<body>

<header class="section hero">
  <div class="photo hero-photo" role="img" aria-label="Engineers in hard hats and high-visibility jackets reviewing plans inside a steel-frame warehouse"></div>
  <div class="topbar"></div>
  <div class="brand"><i class="mark"></i>BIRCHWAY</div>
  <nav class="nav">
    <span class="active" style="left:648px">HOME</span>
    <span style="left:758px">ABOUT</span>
    <span style="left:875px">SERVICES</span>
    <span style="left:1013px">PROJECTS</span>
    <span style="left:1155px">CONTACT</span>
  </nav>
  <div class="abs hero-bar"></div>
  <h1 class="abs hero-title">BIRCHWAY CONTRACTING</h1>
  <p class="abs hero-text">Lorem ipsum dolor sit amet, consectetur adipiscing elit, sed do eiusmod tempor incididunt ut labore et dolore magna aliqua</p>
  <div class="btn" style="left:147px;top:470px;width:188px;height:50px">Get Started</div>
  <div class="dots" style="left:148px;top:543px"><i class="on"></i><i></i><i></i><i></i></div>
</header>

<section class="section welcome">
  <div class="vline" style="top:0;height:55px"></div>
  <h2 class="abs welcome-title">WELCOME TO<br>BIRCHWAY CONTRACTING</h2>
  <p class="abs welcome-text">Sed ut perspiciatis unde omnis iste nrror sit voluptatem accusantium doloremque laudantium,lo inventore veritatis et quasi architecto beae vitae dicta sunt es sit asper aut odit aut fugit, sed quia consequuntur magni dolores ee voluptatem sequi nesciunt. Neque porro quisquam est, qui dolorem ipsum quia dolor sit amet, consectetur, adipisci velit, sed quia non numquam es modi tempora incidunt ut labore et dolore magnam aliquam quaerat voluptatem.</p>
  <div class="btn" style="left:121px;top:424px;width:185px;height:50px">Learn More</div>
  <div class="photo welcome-photo" role="img" aria-label="Two engineers in white hard hats holding plans on a building site with cranes"></div>
  <div class="vline" style="top:520px;height:66px"></div>
</section>

<section class="section band services">
  <h2 class="band-title" style="top:80px">WHAT WE DO</h2>
  <div class="service photo" style="left:112px;background:linear-gradient(180deg,#3f4a5c,#23272e)" role="img" aria-label="Commercial apartment tower"><span style="top:137px">COMMERCIAL</span>
    <svg class="abs" style="left:0;top:0" width="234" height="297"><polyline points="150,8 226,8 226,60" fill="none" stroke="#fff" stroke-width="2"/><polyline points="8,237 8,289 84,289" fill="none" stroke="#fff" stroke-width="2"/></svg></div>
  <div class="service photo" style="left:359px;background:linear-gradient(180deg,#9fb8d8,#5f7a92 55%,#3f6a2c)" role="img" aria-label="Residential house with garden"><span style="top:257px">RESIDENTIAL</span></div>
  <div class="service photo" style="left:606px;background:linear-gradient(180deg,#8a6bb0,#d48aa8 50%,#2a2230)" role="img" aria-label="Industrial plant with chimneys at dusk"><span style="top:257px">INDUSTRIAL</span></div>
  <div class="service photo" style="left:853px;background:linear-gradient(180deg,#7aa0c4,#5a4a3c 50%,#2b2a2a)" role="img" aria-label="Modern bespoke apartment building"><span style="top:257px">ONE-OF-A-KIND</span></div>
</section>

<section class="section news">
  <div class="vline" style="top:3px;height:68px"></div>
  <h2 class="section-title" style="left:0;width:1200px;text-align:center;top:72px">LATEST NEWS</h2>
  <article class="news-card" style="left:120px">
    <div class="photo" style="background:linear-gradient(160deg,#e4e7ea,#b9c0c8 60%,#8f979f)" role="img" aria-label="Hands reviewing construction drawings beside a red hard hat"></div>
    <h3>Finibus Bonorum et Malorum</h3>
    <p>Lorem ipsum dolor sit amet, consecte elit, sed do eiusmod tempor incididunt ut labore et dolore magaliqua. Quis ipsum suspendisse ultrices gravida. Risus commodo</p>
    <div class="btn">Read More</div>
  </article>
  <article class="news-card" style="left:614px">
    <div class="photo" style="background:linear-gradient(170deg,#4f7fb8,#9cb9d8 55%,#2c3440)" role="img" aria-label="Steel building frame and crane against a blue sky"></div>
    <h3>Finibus Bonorum et Malorum</h3>
    <p>Lorem ipsum dolor sit amet, consecte elit, sed do eiusmod tempor incididunt ut labore et dolore magaliqua. Quis ipsum suspendisse ultrices gravida. Risus commodo</p>
    <div class="btn">Read More</div>
  </article>
  <div class="vline" style="top:750px;height:0"></div>
</section>

<section class="section band projects">
  <h2 class="band-title" style="top:82px">THE PROOF IS IN OUR WORK</h2>
  <p class="sub">We like to think that our work can speak for itself.</p>
  <div class="filters">
    <span class="on" style="left:112px">ALL</span>
    <span style="left:190px">EDUCATION</span>
    <span style="left:323px">HEALTHCARE</span>
    <span style="left:469px">INDUSTRIAL</span>
    <span style="left:605px">MANUFACTURING</span>
    <span style="left:783px">OFFICE</span>
    <span style="left:877px">RECREATIONAL</span>
    <span style="left:1034px">RETAIL</span>
  </div>
  <div class="project photo" style="left:112px;background:linear-gradient(180deg,#6c8fb8,#8a6a48 55%,#3a2c20)" role="img" aria-label="Timber-frame house under construction"><span>FINIBUS BONORUM ET</span></div>
  <div class="project project-info" style="left:446px">
    <h4>FINIBUS BONORUM ET</h4>
    <p>Lorem ipsum doloret, consectetur iusmod tempor incidnt ut labore et dolore magna aliqua. Quis ipsum suspendisse ultrices gravida.</p>
  </div>
  <div class="project photo" style="left:780px;background:linear-gradient(180deg,#3f78c0,#a9b4bd 50%,#556050)" role="img" aria-label="New apartment block with trees"><span>FINIBUS BONORUM ET</span></div>
  <div class="dots" style="left:561px;top:592px"><i class="on"></i><i></i><i></i><i></i></div>
</section>

<section class="section team">
  <div class="vline" style="top:0;height:83px"></div>
  <h2 class="section-title" style="left:121px;top:88px">MEET OUR TEAM</h2>
  <div class="member" style="left:112px"><div class="photo" style="background:linear-gradient(180deg,#b9c2c6,#d8e04a 70%,#2c3448)" role="img" aria-label="Team member in white hard hat and hi-vis jacket"></div><h5>JOHN SMITH</h5><div class="rule"></div><p>Chief executive officer</p></div>
  <div class="member" style="left:359px"><div class="photo" style="background:linear-gradient(180deg,#c48a5a,#e0d840 70%,#d8dbe0)" role="img" aria-label="Team member in yellow hard hat and hi-vis vest"></div><h5>JOHN SMITH</h5><div class="rule"></div><p>Chief executive officer</p></div>
  <div class="member" style="left:606px"><div class="photo" style="background:linear-gradient(180deg,#3a62c0,#9aa6b0 40%,#d0dc40)" role="img" aria-label="Team member in blue hard hat and hi-vis vest"></div><h5>JOHN SMITH</h5><div class="rule"></div><p>Chief executive officer</p></div>
  <div class="member" style="left:853px"><div class="photo" style="background:linear-gradient(180deg,#c87a5a,#e0d840 70%,#d8dbe0)" role="img" aria-label="Team member in yellow hard hat and hi-vis vest"></div><h5>JOHN SMITH</h5><div class="rule"></div><p>Chief executive officer</p></div>
</section>

<section class="section band contact">
  <h2 class="band-title" style="top:98px">GET IN TOUCH</h2>
  <div class="field" style="left:205px;top:177px;width:385px;height:48px">First Name</div>
  <div class="field" style="left:606px;top:177px;width:386px;height:48px">Last Name</div>
  <div class="field" style="left:205px;top:243px;width:385px;height:48px">Email</div>
  <div class="field" style="left:606px;top:243px;width:386px;height:48px">Phone</div>
  <div class="field area" style="left:205px;top:311px;width:787px;height:104px">How Can We Help?</div>
  <div class="submit">SUBMIT</div>
</section>

<footer class="section footer">
  <div class="abs foot-brand"><i class="mark"></i>BIRCHWAY</div>
  <div class="socials"><i></i><i></i><i></i><i></i></div>
  <div class="foot-col" style="left:389px">
    <h6>QUICK LINKS</h6><div class="rule"></div>
    <ul><li>Home</li><li>About</li><li>Services</li><li>Projects</li><li>Contact</li></ul>
  </div>
  <div class="foot-col" style="left:560px">
    <h6>CONTACT DETAILS</h6><div class="rule"></div>
    <div class="contact-row"><svg width="34" height="34" viewBox="0 0 34 34"><circle cx="17" cy="17" r="17" fill="#e8241b"/><path d="M17 8a6 6 0 0 0-6 6c0 5 6 12 6 12s6-7 6-12a6 6 0 0 0-6-6zm0 8.5a2.5 2.5 0 1 1 0-5 2.5 2.5 0 0 1 0 5z" fill="#fff"/></svg><span>123 Your Adress Goes Here.<br>USA, 1234567</span></div>
    <div class="contact-row"><svg width="34" height="34" viewBox="0 0 34 34"><circle cx="17" cy="17" r="17" fill="#e8241b"/><path d="M12 9l3 0 1.5 4-2 1.5a9 9 0 0 0 4 4l1.5-2 4 1.5v3c0 1-1 2-2 2A13 13 0 0 1 10 11c0-1 1-2 2-2z" fill="#fff"/></svg><span style="line-height:34px">204-555-0148</span></div>
    <div class="contact-row"><svg width="34" height="34" viewBox="0 0 34 34"><circle cx="17" cy="17" r="17" fill="#e8241b"/><rect x="9" y="11" width="16" height="12" rx="1" fill="#fff"/><path d="M9 12l8 6 8-6" fill="none" stroke="#e8241b" stroke-width="1.5"/></svg><span style="line-height:34px">info@BirchwayContracting.com</span></div>
  </div>
  <div class="foot-col" style="left:947px">
    <h6>LOCATION MAP</h6><div class="rule"></div>
    <ul><li>Projects Info</li><li>Our Clients</li><li>Complete Projects</li><li>Certifications</li><li>Terms &amp; Conditon</li><li>Privacy Policy</li></ul>
  </div>
  <div class="foot-rule"></div>
  <p class="copy">© 2022 Birchway Contracting. All Rights Reserved</p>
</footer>

</body>
</html>
```